Trade Show Poster/Booth Backdrop for Rugged Technology Business

I need a graphic design for an 8' x 6' poster to hang on back wall of my event booth. Design must be consistent with my company's colors, logo, and current branding as shown on website, Facebook, and Twitter (links provided). You can propose other elements, but there are certain core images and text elements that must be incorporated. Print specifications also provided. File must be delivered on time and upload-ready.

Font styles to use
Sans Serif

Colors
33a6d7
0355a3
33b8a4
00a990
9bcb3b
abd036
cadf82
85cae6
86cfc6

Requirements
Nice to have
• Regarding color, I'm okay with designs using the orange version of the Morvex logo.
• Regarding the images I provided as potential background layers, I especially like the ones with rocky island profiles and exposed cliff faces. In addition to being a nice match color wise, they are subtle suggestions of ruggedness and working with technology that can handle extreme environments (which is a big part of the messaging focus).
Should not have
• Vibrant coloration is very much desired and OK, but please avoid a blend that goes to either extreme. For instance, too much dark blue makes it look like every other tech company ever. Too much warm, light green (other than for contrast elements) makes it look too tropical and casual.

```html
<!DOCTYPE html>
<html lang="en">
<head>
<meta charset="utf-8">
<title>Kestrel Enterprises – Booth Backdrop</title>
<link rel="stylesheet" href="https://fonts.googleapis.com/css2?family=Arimo:wght@400;700&display=swap">
<style>
  :root {
    --deep-blue: #2b5eb0;
    --sky-blue: #33a6d7;
    --teal: #33b8a4;
    --sea-green: #00a990;
    --leaf-green: #9bcb3b;
    --lime: #abd036;
    --pale-lime: #cadf82;
    --text-light: #ffffff;
    --partner-grey: #5b5c5e;
    --brand-green: #4aa83a;
    --partner-blue: #1c8fd0;
    --paper: #ffffff;
  }
  * { margin: 0; padding: 0; box-sizing: border-box; }
  html, body {
    width: 1200px;
    height: 900px;
    overflow: hidden;
    background: var(--paper);
  }
  .backdrop {
    position: relative;
    width: 1200px;
    height: 900px;
    font-family: "Arimo", Arial, sans-serif;
    background: var(--paper);
  }
  .hero {
    position: absolute;
    left: 0;
    top: 0;
    width: 1200px;
    height: 707px;
    overflow: hidden;
  }
  .hero-scene {
    position: absolute;
    inset: 0;
    background:
      linear-gradient(180deg, rgba(255,255,255,0.10) 0%, rgba(255,255,255,0) 35%, rgba(0,40,60,0.10) 100%),
      linear-gradient(100deg,
        var(--deep-blue) 0%,
        #3b86c2 14%,
        #3fb0b2 34%,
        #5ec39a 50%,
        #8cc85a 68%,
        var(--leaf-green) 84%,
        #86b83c 100%);
  }
  .headline {
    position: absolute;
    top: 351px;
    left: 0;
    width: 1200px;
    text-align: center;
    color: var(--text-light);
    font-size: 30px;
    font-weight: 400;
    letter-spacing: 0.1px;
  }
  .offerings {
    position: absolute;
    top: 412px;
    left: 218px;
    width: 758px;
    display: flex;
    justify-content: space-between;
    list-style: none;
    color: var(--text-light);
    font-size: 22px;
  }
  .social-handle {
    position: absolute;
    top: 660px;
    left: 0;
    width: 1200px;
    text-align: center;
    color: var(--text-light);
    font-size: 29px;
  }
  .partners {
    position: absolute;
    left: 0;
    top: 707px;
    width: 1200px;
    height: 193px;
    background: var(--paper);
  }
  .partner {
    position: absolute;
    display: flex;
    align-items: center;
    gap: 10px;
    font-family: "Arimo", Arial, sans-serif;
    font-weight: 700;
    white-space: nowrap;
    transform: translate(-50%, -50%);
  }
  .partner-morvex {
    left: 296px;
    top: 97px;
    font-size: 46px;
    color: var(--partner-grey);
    letter-spacing: -1px;
  }
  .partner-kestrel {
    left: 600px;
    top: 97px;
    flex-direction: column;
    gap: 8px;
    color: var(--brand-green);
    font-size: 30px;
    letter-spacing: 3px;
    line-height: 1.05;
    text-align: center;
  }
  .partner-kestrel .mark-dot {
    width: 52px;
    height: 52px;
    border-radius: 50%;
    background: var(--sky-blue);
  }
  .partner-vantor {
    left: 938px;
    top: 97px;
    font-size: 30px;
    color: var(--partner-blue);
  }
  .partner-vantor .mark-dot {
    width: 40px;
    height: 40px;
    border-radius: 50%;
    background: var(--partner-blue);
  }
</style>
</head>
<body>
  <main class="backdrop">
    <section class="hero">
      <div class="hero-scene" role="img" aria-label="Photograph of rocky tropical islands and a forested coastline under a cloudy sky, tinted with a blue-to-green gradient"></div>
      <h1 class="headline">Fully Rugged &amp; Business Class Technology Solutions</h1>
      <ul class="offerings">
        <li>Mobility</li>
        <li>Computing</li>
        <li>Mounting</li>
        <li>Printing</li>
        <li>Imaging</li>
        <li>Storage</li>
      </ul>
      <p class="social-handle">@KestrelforIT</p>
    </section>
    <footer class="partners">
      <div class="partner partner-morvex">Morvex</div>
      <div class="partner partner-kestrel">
        <span class="mark-dot"></span>
        <span>KESTREL<br>Enterprises</span>
      </div>
      <div class="partner partner-vantor">
        <span class="mark-dot"></span>
        <span>Vantor</span>
      </div>
    </footer>
  </main>
</body>
</html>
```